Tease by Dusk Age Verification Landing Page

To create a visually appealing design for the landing page of the adult game "Tease by Dusk" that confirms the visitor's age.
The design should have a simple and visually appealing look that focuses on two buttons labeled "Yes" and "No". The purpose of the page is to confirm that the visitor is 18 years of age or older before accessing the game's content. Responsive design that works well on desktop and mobile devices. The final output should be delivered in PSD, AI, or Sketch format, along with any necessary images or assets.
I have also attached examples.

```html
<!DOCTYPE html>
<html lang="en">
<head>
<meta charset="utf-8">
<title>Tease by Dusk — Age Verification</title>
<link href="https://fonts.googleapis.com/css2?family=Inter:wght@400;500;600;700&display=swap" rel="stylesheet">
<style>
  :root {
    --bg-deep: #050505;
    --bg-mid: #1a1a1c;
    --bg-warm: #1b0808;
    --panel: rgba(8, 8, 9, 0.88);
    --text-main: #d9d9d9;
    --text-muted: #a8a8a8;
    --brand-purple: #7e4a8b;
    --brand-red: #a81e2c;
  }
  * { box-sizing: border-box; margin: 0; padding: 0; }
  html, body { width: 1200px; height: 1200px; overflow: hidden; background: var(--bg-deep); }
  body { font-family: "Inter", sans-serif; color: var(--text-main); position: relative; }

  .backdrop {
    position: absolute; inset: 0;
    background:
      radial-gradient(ellipse 420px 260px at 600px 360px, rgba(70,62,60,0.55), transparent 70%),
      linear-gradient(180deg, #0a0b0d 0%, #141518 30%, #1e1e20 52%, #252425 62%, #1a1112 72%, var(--bg-warm) 82%, var(--bg-deep) 100%);
  }

  .age-gate {
    position: absolute; left: 335px; top: 222px; width: 488px; height: 372px;
    background: var(--panel);
    border-radius: 12px;
    display: flex; flex-direction: column; align-items: center;
  }
  .brand-name {
    margin-top: 36px;
    font-size: 30px; font-weight: 600; line-height: 1;
    color: var(--brand-purple);
    letter-spacing: -0.5px;
  }
  .tagline {
    margin-top: 12px;
    width: 394px; height: 66px;
    border-radius: 34px;
    border: 1.5px solid transparent;
    background:
      linear-gradient(#080809, #080809) padding-box,
      linear-gradient(90deg, var(--brand-purple), var(--brand-red)) border-box;
    display: flex; align-items: center; justify-content: center;
    font-size: 31px; font-weight: 600; color: var(--text-main);
  }
  .notice {
    margin-top: 27px;
    font-size: 17px; font-weight: 400; color: var(--text-main);
    text-align: center; line-height: 1;
  }
  .question { margin-top: 19px; }
  .choices {
    margin-top: 25px;
    width: 488px; height: 49px; position: relative;
  }
  .choice {
    position: absolute; top: 0; height: 49px;
    border: none; border-radius: 4px;
    font-family: "Inter", sans-serif; font-size: 23px; font-weight: 600;
    letter-spacing: 3px;
    display: flex; align-items: center; justify-content: center;
  }
  .choice-no { left: 60px; width: 150px; background: none; color: var(--text-muted); }
  .choice-yes {
    left: 244px; width: 218px;
    background: linear-gradient(90deg, var(--brand-purple) 0%, #7f4a86 40%, var(--brand-red) 100%);
    color: var(--text-main);
  }
  .remember {
    margin-top: 14px;
    display: flex; align-items: center; gap: 11px;
    font-size: 13.5px; color: var(--text-main);
  }
  .remember svg { display: block; }
</style>
</head>
<body>
  <div class="backdrop" role="img" aria-label="Dimmed photograph of a person lying forward with arms stretched out, fading into a dark red floor"></div>

  <main class="age-gate">
    <div class="brand-name">Tease by Dusk</div>
    <div class="tagline">Dirty games</div>
    <p class="notice">You’re going to see a lot of strip varations at home.</p>
    <p class="notice question">Can you handle this?</p>
    <div class="choices">
      <button class="choice choice-no">NO</button>
      <button class="choice choice-yes">YES</button>
    </div>
    <label class="remember">
      <svg width="16" height="16" viewBox="0 0 16 16"><circle cx="8" cy="8" r="7" fill="none" stroke="#d9d9d9" stroke-width="1.3"/></svg>
      Remember me
    </label>
  </main>
</body>
</html>
```